Astrological planner&diary book cover.

Book cover for print paperback. Title: "Whole Stargazer Journal & Logbook – Sign One (Sign Two, Sign Three etc) 2022: Shape your days by charting Orbital and Night angles and passages, Idle Drift, Night cycles, Sky almanac, and Reversing bodies." The book is a series of Astrological diary & planner for 2022 for each Zodiac sign (12 books in total). The design template should be the same – the only difference would be the Zodiac sign image and text.
It should be neutral to positive. There is no restriction regarding the colors – it can be both B&W and full color.
The design should be original and not include any images which require obtaining a copyright license to use. Symbols in common use and not copyrighted are probably ok.
Text for the back cover is not yet available, will be ready by the end of the project. I will need PDF, JPEG, TIFF (all formats both in CMYK and RGB), and the source file. For CMYK, we need files with no color profiles assigned.
I have several options in my mind (But please do not limit yourself by these options - please feel free to suggest your vision):
1) Is Gradient morning clear sky and the star constellation and image at skyrise (like a rising star)
2) solid dark color with image and symbols of the Zodiac sign
75% of my auditory are women

```html
<!DOCTYPE html>
<html lang="en">
<head>
<meta charset="utf-8">
<title>Whole Stargazer Journal &amp; Logbook – Sign One 2022</title>
<link rel="stylesheet" href="https://fonts.googleapis.com/css2?family=Bebas+Neue&family=Montserrat:wght@400;600;700&display=swap">
<style>
  :root {
    --page-bg: #242424;
    --sky-deep: #1a0a52;
    --sky-mid: #3a1490;
    --sky-glow: #6a2fc0;
    --line: #e9e4ff;
    --white: #ffffff;
    --gold-light: #f6d77a;
    --gold: #d9a93a;
    --gold-dark: #a8741c;
  }
  * { margin: 0; padding: 0; box-sizing: border-box; }
  html, body {
    width: 720px; height: 1200px; overflow: hidden;
    background: var(--page-bg);
  }
  .cover {
    position: absolute; left: 0; top: 60px;
    width: 720px; height: 1080px;
    background:
      radial-gradient(ellipse 55% 30% at 50% 62%, var(--sky-glow) 0%, transparent 70%),
      radial-gradient(ellipse 60% 25% at 65% 14%, rgba(140, 70, 210, .55) 0%, transparent 70%),
      linear-gradient(180deg, var(--sky-deep) 0%, var(--sky-mid) 45%, var(--sky-deep) 100%);
    text-align: center;
    color: var(--white);
  }
  .cover-frame { position: absolute; inset: 0; }
  .kicker {
    position: absolute; top: 82px; left: 0; right: 0;
    display: flex; align-items: center; justify-content: center; gap: 16px;
    font: 600 42px/1 "Montserrat", sans-serif; letter-spacing: 1px;
  }
  .rule { display: block; width: 58px; height: 2px; background: var(--line); }
  .rule--long { width: 130px; }
  .gold {
    background: linear-gradient(180deg, var(--gold-light) 0%, var(--gold) 50%, var(--gold-dark) 100%);
    -webkit-background-clip: text; background-clip: text; color: transparent;
  }
  .title-main {
    position: absolute; top: 146px; left: 0; right: 0;
    font: 400 94px/1 "Bebas Neue", sans-serif; letter-spacing: 2px;
  }
  .title-sub {
    position: absolute; top: 250px; left: 0; right: 0;
    font: 700 36px/1 "Montserrat", sans-serif; letter-spacing: 1px;
  }
  .sign-line {
    position: absolute; top: 315px; left: 0; right: 0;
    font: 400 41px/1 "Bebas Neue", sans-serif; letter-spacing: .5px;
  }
  .year {
    position: absolute; top: 383px; left: 0; right: 0;
    display: flex; align-items: center; justify-content: center; gap: 34px;
    font: 700 44px/1 "Montserrat", sans-serif;
  }
  .sign-wheel {
    position: absolute; left: 164px; top: 484px;
    width: 384px; height: 384px; border-radius: 50%;
    background: radial-gradient(circle, #8a48d8 0%, #5a22a8 55%, #3a1490 100%);
    box-shadow: 0 0 60px rgba(150, 90, 230, .45);
  }
  .tagline {
    position: absolute; top: 916px; left: 90px; right: 90px;
    font: 400 15px/1.3 "Montserrat", sans-serif;
  }
</style>
</head>
<body>
  <main class="cover">
    <svg class="cover-frame" width="720" height="1080" viewBox="0 0 720 1080" aria-hidden="true">
      <path d="M100 39 H625 A40 40 0 0 0 673 87 V993 A40 40 0 0 0 625 1041 H100 A40 40 0 0 0 52 993 V87 A40 40 0 0 0 100 39 Z"
            fill="none" stroke="var(--line)" stroke-width="2"/>
      <path d="M86 29 H639 V35 M86 29 V35" fill="none" stroke="none"/>
    </svg>

    <p class="kicker"><span class="rule"></span>WHOLE<span class="rule"></span></p>
    <h1 class="title-main gold">STARGAZER</h1>
    <p class="title-sub gold">JOURNAL &amp; LOGBOOK</p>
    <p class="sign-line">SIGN ONE (SIGN TWO, SIGN THREE ETC)</p>
    <p class="year"><span class="rule rule--long"></span>2022<span class="rule rule--long"></span></p>

    <div class="sign-wheel" role="img" aria-label="Zodiac wheel illustration with the twelve sign symbols around a sacred geometry star"></div>

    <p class="tagline">Shape your days by charting Orbital and Night angles and passages, Idle Drift, Night cycles, Sky almanac, and Reversing bodies.</p>
  </main>
</body>
</html>
```